Ridgeway Hearth Partners Business Card

Looking for a new business card layout. We are a real estate firm w/ a logo, old design attached. Must keep the same elements on there, just need a fresh look and possible some foil accents. Looking for a simpler design w/ more modern style.

Target Market(s)

Real Estate clients

Industry/Entity Type

Real Estate Agent

Contact Information for Business Card

Font styles to use
Sans Serif

Requirements
Must have
• all elements on current biz card
Nice to have
• modern look, simpler than we have!
Should not have
• no serif fonts

```html
<!DOCTYPE html>
<html lang="en">
<head>
<meta charset="utf-8">
<title>Ridgeway Hearth Partners Business Card</title>
<link rel="stylesheet" href="https://fonts.googleapis.com/css2?family=PT+Sans:wght@400;700&family=Yellowtail&display=block">
<style>
  :root {
    --frame: #2a2927;
    --paper: #ffffff;
    --stage-grey: #b2b4b3;
    --card-dark: #2a2927;
    --gold: #a8842a;
    --silver: #a9a8a6;
    --aqua: #43bccd;
    --ink: #222222;
    --white: #ffffff;
    --card-edge: #9a9a9a;
  }
  * { box-sizing: border-box; margin: 0; padding: 0; }
  html, body { width: 1200px; height: 1200px; overflow: hidden; background: var(--frame); }
  body { font-family: "PT Sans", sans-serif; color: var(--ink); }
  .board { position: relative; width: 1200px; height: 1200px; background: var(--frame); }
  .band { position: absolute; left: 27px; width: 1146px; }
  .band--light { top: 27px; height: 520px; background: var(--paper); }
  .band--grey { top: 547px; height: 520px; background: var(--stage-grey); }
  .band--caption { top: 1067px; height: 106px; background: var(--paper); }

  .card { position: absolute; width: 252px; height: 144px; overflow: hidden; }
  .card--front-white { left: 329px; top: 215px; background: var(--paper); border: 1px solid var(--card-edge); }
  .card--back-dark-a { left: 619px; top: 215px; background: var(--card-dark); color: var(--white); }
  .card--front-photo { left: 329px; top: 735px; background: var(--aqua); border: 1px solid #6c8f95; }
  .card--back-dark-b { left: 619px; top: 735px; background: var(--card-dark); color: var(--white); }

  .wordmark { font-family: "PT Sans", sans-serif; font-weight: 700; color: var(--gold); text-transform: uppercase; line-height: 1; letter-spacing: 0.04em; white-space: nowrap; }

  .front-white__mark { position: absolute; left: 0; right: 0; top: 48px; text-align: center; font-size: 21px; }
  .front-white__url { position: absolute; left: 0; right: 0; top: 101px; text-align: center; font-size: 9.5px; letter-spacing: 0.06em; color: var(--ink); }

  .contact__name { font-weight: 700; font-size: 12.5px; line-height: 1.1; }
  .contact__role { font-size: 6.5px; margin-top: 1px; }
  .contact__grid { display: grid; grid-template-columns: 28px auto; font-size: 7.5px; line-height: 1.3; }
  .contact__label { font-size: 6.5px; }
  .contact__addr { font-size: 7.5px; line-height: 1.3; }

  .back-a__block { position: absolute; left: 118px; top: 12px; }
  .back-a__block .contact__grid { margin-top: 8px; }
  .back-a__block .contact__addr { margin-top: 11px; }
  .back-a__mark { position: absolute; left: 14px; top: 112px; font-size: 11px; color: var(--silver); }

  .back-b__block { position: absolute; left: 16px; top: 12px; }
  .back-b__block .contact__grid { margin-top: 8px; }
  .back-b__addr { position: absolute; left: 113px; top: 46px; }
  .back-b__mark { position: absolute; left: 0; right: 0; top: 80px; font-size: 18px; text-align: center; }
  .back-b__url { position: absolute; left: 0; right: 0; top: 124px; text-align: center; font-size: 8.5px; letter-spacing: 0.14em; text-transform: uppercase; }

  .front-photo__portrait { position: absolute; left: 0; top: 0; width: 125px; height: 144px; }
  .front-photo__greeting { position: absolute; left: 113px; top: 30px; font-family: "Yellowtail", sans-serif; color: var(--ink); line-height: 1.1; transform: rotate(-6deg); transform-origin: left top; white-space: nowrap; }
  .front-photo__greeting .line-sm { display: block; font-size: 14px; }
  .front-photo__greeting .line-lg { display: block; font-size: 21px; }
  .front-photo__greeting .line-md { display: block; font-size: 13px; }

  .caption__mark { position: absolute; left: 381px; width: 384px; top: 40px; font-size: 24px; text-align: center; letter-spacing: 0.02em; }
  .caption__rule { position: absolute; left: 804px; top: 19px; width: 1px; height: 70px; background: var(--ink); }
  .caption__label { position: absolute; left: 847px; top: 43px; font-size: 15px; letter-spacing: 0.16em; color: var(--ink); }
</style>
</head>
<body>
<main class="board">
  <section class="band band--light"></section>
  <section class="band band--grey"></section>
  <section class="band band--caption">
    <div class="wordmark caption__mark">Ridgeway Hearth Partners</div>
    <div class="caption__rule"></div>
    <div class="caption__label">GOLDEN FOIL</div>
  </section>

  <article class="card card--front-white">
    <div class="wordmark front-white__mark">Ridgeway Hearth<br>Partners</div>
    <div class="front-white__url">RidgewayHearth-Homes.com</div>
  </article>

  <article class="card card--back-dark-a">
    <div class="back-a__block">
      <div class="contact__name">Marla Quinn</div>
      <div class="contact__role">Principal Broker</div>
      <div class="contact__grid">
        <span class="contact__label">cell</span><span>555.210.4418</span>
        <span class="contact__label">office</span><span>555.318.6620</span>
        <span></span><span>marla@ridgewayhearth.com</span>
      </div>
      <div class="contact__addr">82 NE Alder Ave.,<br>Brookfield, OR 97000</div>
    </div>
    <div class="wordmark back-a__mark">Ridgeway Hearth Partners</div>
  </article>

  <article class="card card--front-photo">
    <svg class="front-photo__portrait" viewBox="0 0 125 144" role="img" aria-label="Portrait photograph of the broker">
      <defs>
        <linearGradient id="portraitTone" x1="0" y1="0" x2="1" y2="1">
          <stop offset="0" stop-color="#e6ddd2"/>
          <stop offset="1" stop-color="#c9a985"/>
        </linearGradient>
      </defs>
      <polygon points="0,0 110,0 125,144 0,144" fill="url(#portraitTone)"/>
    </svg>
    <div class="front-photo__greeting">
      <span class="line-sm">Hi</span>
      <span class="line-sm">I am</span>
      <span class="line-lg">Marla Quinn</span>
      <span class="line-md">your property broker</span>
    </div>
  </article>

  <article class="card card--back-dark-b">
    <div class="back-b__block">
      <div class="contact__name">Marla Quinn</div>
      <div class="contact__role">Principal Broker</div>
      <div class="contact__grid">
        <span class="contact__label">cell</span><span>555.210.4418</span>
        <span class="contact__label">office</span><span>555.318.6620</span>
      </div>
      <div class="contact__addr">marla@ridgewayhearth.com</div>
    </div>
    <div class="contact__addr back-b__addr">82 NE Alder Ave.,<br>Brookfield, OR 97000</div>
    <div class="wordmark back-b__mark">Ridgeway Hearth<br>Partners</div>
    <div class="back-b__url">RidgewayHearth-Homes.com</div>
  </article>
</main>
</body>
</html>
```